Wine Label Design for a white wine made in the region of San Gimignano, Italy

This is a white wine (crisp and fresh) that is made in the region of San Gimignano, Italy, which is a beautiful hill town in Tuscany famous for it's towers. We would like a classy, elegant front wine label that can also be somewhat fun and whimsical if you prefer. Showcasing or depicting or alluding to the town and the towers of San Gimignano is a plus. The label should state the brand name which is "Cortivane", the varietal, which is Vernaccia di San Gimignano, and the vintage which is 2015. We might change the size of the label slightly but for design purposes please use 5 inches wide x 5 1/2 inches tall. I've uploaded a photo of a successful label design for parameters, but you should not feel limited to this either. Good white wine colors are white and green but we are flexible. Please don't use red, burgundy, or blue colors.

Target Market(s)

This wine label should appeal to all ages but be classy for the older crowd and still eye catching and fun for the millennials. This wine is sold in 15 states in the US, on the East Coast.

Industry/Entity Type

Town

Font styles to use
Serif
Sans Serif

Requirements
Must have
• Referring somehow or depicting the hill town and towers of San Gimignano in some way, such as in silhouette would be a plus. But also try to do something fun and unique with it-- not just an image of the town with words placed over it.
Should not have
• Please don't use the colors blue, reds. Try to think about what makes a wine label classy and sophisticated and 'upmarket' and what makes one cheap and cheesy. We are looking for the classy and sophisticated.

```html
<!DOCTYPE html>
<html lang="en">
<head>
<meta charset="utf-8">
<title>Cortivane – Vernaccia di San Gimignano 2015</title>
<link href="https://fonts.googleapis.com/css2?family=Questrial&family=Allura&display=swap" rel="stylesheet">
<style>
  :root {
    --canvas: #ffffff;
    --label-green: #a3a63f;
    --label-white: #ffffff;
    --ink-green: #9ea23a;
  }
  * { margin: 0; padding: 0; box-sizing: border-box; }
  html, body {
    width: 1200px;
    height: 1089px;
    overflow: hidden;
    background: var(--canvas);
  }
  .canvas {
    position: relative;
    width: 1200px;
    height: 1089px;
  }
  .wine-label {
    position: absolute;
    left: 190px;
    top: 93px;
    width: 820px;
    height: 902px;
    background: var(--label-green);
    overflow: hidden;
  }
  .grape-emblem {
    position: absolute;
    left: 346px;
    top: 48px;
    width: 128px;
    height: 213px;
    background: var(--label-white);
    border-radius: 46% 46% 50% 50% / 30% 30% 70% 70%;
  }
  .brand-name {
    position: absolute;
    left: 0;
    right: 0;
    top: 410px;
    text-align: center;
    font-family: "Questrial", sans-serif;
    font-size: 66px;
    line-height: 1;
    letter-spacing: 6px;
    color: var(--label-white);
  }
  .landscape {
    position: absolute;
    left: 0;
    top: 0;
    width: 820px;
    height: 902px;
  }
  .town-skyline {
    position: absolute;
    left: 287px;
    top: 635px;
    width: 377px;
    height: 130px;
    background: linear-gradient(to bottom, rgba(255,255,255,0.85), var(--label-white));
  }
  .varietal {
    position: absolute;
    left: 0;
    right: 0;
    top: 784px;
    text-align: center;
    font-family: "Allura", cursive;
    font-size: 40px;
    line-height: 1;
    color: var(--ink-green);
  }
  .vintage {
    position: absolute;
    left: 0;
    right: 0;
    top: 816px;
    text-align: center;
    font-family: "Allura", cursive;
    font-size: 46px;
    line-height: 1;
    color: var(--ink-green);
  }
</style>
</head>
<body>
<main class="canvas">
  <section class="wine-label">
    <div class="grape-emblem" role="img" aria-label="White grape bunch with vine leaf emblem"></div>
    <h1 class="brand-name">CORTIVANE</h1>
    <div class="town-skyline" role="img" aria-label="White silhouette of the towers of San Gimignano"></div>
    <svg class="landscape" viewBox="0 0 820 902" aria-hidden="true">
      <path d="M0 757 Q410 700 820 757 L820 870 L0 870 Z" fill="#ffffff"/>
    </svg>
    <p class="varietal">vernaccia di san gimignano</p>
    <p class="vintage">2015</p>
  </section>
</main>
</body>
</html>
```